New Company Business Card Design

I have a new company logo and I want a new business card design. I dont know if the logo file i attached is in the correct format or quality. We are a New York City Specialty construction Firm specializing in high risk out of the box projects. I want a simple and classy business card that people will his card is as crisp as the work his company does.

Target Market(s)

Clients in the heavy construction industry in New York City

Industry/Entity Type

Construction Company

Contact Information for Business Card

Simple Classy - DIFFERENT

Font styles to use
Other font styles liked:
• Mach the logo font in some way

Colors

Designer to choose colors to be used in the design.

Requirements
Must have
• Uniqueness
Nice to have
• Nothing particular - Just different and classy - Timeless
Should not have
• Goofy Shit or Gimmicky shit

```html
<!DOCTYPE html>
<html lang="en">
<head>
<meta charset="UTF-8">
<title>Keystrand Builders – Business Card</title>
<link href="https://fonts.googleapis.com/css2?family=Open+Sans:wght@400;700;800&display=swap" rel="stylesheet">
<style>
  :root {
    --backdrop: #8c8c8c;
    --card: #ffffff;
    --card-back: #fafbfa;
    --navy: #1f3c6d;
    --ink: #2a2f38;
  }
  * { box-sizing: border-box; margin: 0; padding: 0; }
  html, body { width: 1200px; height: 912px; overflow: hidden; }
  body {
    background: var(--backdrop);
    font-family: "Open Sans", Arial, sans-serif;
    position: relative;
  }
  .card {
    position: absolute;
    width: 525px;
    height: 300px;
    background: var(--card);
    box-shadow: 0 6px 18px rgba(0,0,0,0.25);
  }
  .card--front { left: 70px; top: 110px; }
  .card--back { left: 605px; top: 500px; background: var(--card-back); }

  .wordmark {
    position: absolute;
    display: flex;
    align-items: center;
    gap: 10px;
    color: var(--navy);
    font-weight: 800;
    letter-spacing: 1px;
  }
  .wordmark__square { width: 22px; height: 22px; background: var(--navy); }
  .card--front .wordmark { left: 48px; top: 112px; font-size: 42px; }
  .card--front .footer-name {
    position: absolute; right: 30px; bottom: 28px;
    color: var(--navy); font-size: 15px; letter-spacing: 0.3px;
  }

  .holder { position: absolute; left: 44px; top: 44px; }
  .holder__name { color: var(--navy); font-weight: 700; font-size: 24px; letter-spacing: 1px; }
  .holder__title { color: var(--ink); font-size: 9.5px; margin-top: 2px; letter-spacing: 0.2px; }
  .card--back .wordmark { left: 44px; top: 180px; font-size: 34px; }

  .contacts {
    position: absolute; left: 300px; top: 46px;
    list-style: none; display: flex; flex-direction: column; gap: 12px;
  }
  .contacts li { display: flex; align-items: flex-start; gap: 10px; color: var(--ink); font-size: 12px; line-height: 1.3; }
  .icon {
    flex: none; width: 20px; height: 20px; border-radius: 4px;
    background: var(--navy); display: flex; align-items: center; justify-content: center;
  }
  .icon svg { width: 12px; height: 12px; }
  .card--back .footer-name {
    position: absolute; right: 26px; bottom: 18px;
    color: var(--ink); font-size: 10px;
  }
</style>
</head>
<body>
  <section class="card card--front" aria-label="Card front">
    <div class="wordmark"><span class="wordmark__square"></span>KEYSTRAND</div>
    <div class="footer-name">KEYSTRAND BUILDERS, INC</div>
  </section>

  <section class="card card--back" aria-label="Card back">
    <div class="holder">
      <div class="holder__name">EVAN MARLOW</div>
      <div class="holder__title">CEO OF KEYSTRAND BUILDERS, INC</div>
    </div>
    <div class="wordmark"><span class="wordmark__square"></span>KEYSTRAND</div>

    <ul class="contacts">
      <li>
        <span class="icon"><svg viewBox="0 0 12 12"><path fill="#fff" d="M2.5 1l2 2-1 1.3c.6 1.4 1.8 2.6 3.2 3.2l1.3-1 2 2-1.3 1.5C5.5 9.8 2.2 6.5 1 3.3z"/></svg></span>
        <span>555-014-2287<br>555-018-3390</span>
      </li>
      <li>
        <span class="icon"><svg viewBox="0 0 12 12"><rect x="1" y="2.5" width="10" height="7" fill="none" stroke="#fff" stroke-width="1.2"/><path d="M1 3l5 3.5L11 3" fill="none" stroke="#fff" stroke-width="1.2"/></svg></span>
        <span>tom@keystrand.com</span>
      </li>
      <li>
        <span class="icon"><svg viewBox="0 0 12 12"><circle cx="6" cy="6" r="4.5" fill="none" stroke="#fff" stroke-width="1.2"/><path d="M1.5 6h9M6 1.5c-2 2.5-2 6.5 0 9M6 1.5c2 2.5 2 6.5 0 9" fill="none" stroke="#fff" stroke-width="1"/></svg></span>
        <span>keystrand.com</span>
      </li>
      <li>
        <span class="icon"><svg viewBox="0 0 12 12"><path fill="#fff" d="M6 1a3.5 3.5 0 0 1 3.5 3.5C9.5 7 6 11 6 11S2.5 7 2.5 4.5A3.5 3.5 0 0 1 6 1z"/><circle cx="6" cy="4.5" r="1.3" fill="#1f3c6d"/></svg></span>
        <span>Thomas R. Calloway<br>118 Harbor Line Road<br>– Linden, New Jersey 07036</span>
      </li>
    </ul>
    <div class="footer-name">KEYSTRAND BUILDERS, INC</div>
  </section>
</body>
</html>
```